Simple Business Cards for Self-employed Coach

Simple business card with a design that includes the QLT logo.
Using either only the logo color or additional colors that match the logo.

Meridian Guides reach deeply into the past, gathering wisdom from East and West, while still staying current with the frontiers of new discovery in cognitive science, genetics, and other disciplines. see https://www.brightharborpath.example/what-is-integral-coaching/

Target Market(s)

Coaching Clients in Tokyo /Asia; in business organizations, but also outside

Industry/Entity Type

Life Coaching

Contact Information for Business Card

Lukas Brenning
Certified Meridian Guide

3-2-48 Kamiyoshi
Nakarino 164-0392
Tokyo, Japan

Phone: +81 70 4817 5062
E-Mail: lukas.brenning@mailora.example

Font styles to use
Sans Serif

Colors
00a990

Requirements
Must have
• include uploaded logo
• color fitting with QLT logo color
Nice to have
• simple, elegant design
Should not have
• clutter

```html
<!DOCTYPE html>
<html lang="en">
<head>
<meta charset="UTF-8">
<title>Lukas Brenning – Certified Meridian Guide</title>
<link rel="stylesheet" href="https://fonts.googleapis.com/css2?family=Arimo:wght@400;700&display=swap">
<style>
  :root {
    --teal: #007a6f;
    --teal-light: #0a8a7e;
    --ink: #111111;
    --paper: #ffffff;
  }
  html, body {
    margin: 0;
    padding: 0;
    overflow: hidden;
    background: var(--paper);
  }
  .card {
    position: relative;
    width: 1200px;
    height: 777px;
    background: var(--paper);
    overflow: hidden;
    font-family: "Arimo", Arial, sans-serif;
    color: var(--ink);
  }
  .brand {
    position: absolute;
    left: 60px;
    top: 54px;
    display: flex;
    align-items: center;
    gap: 18px;
  }
  .brand-square {
    width: 66px;
    height: 66px;
    background: var(--teal);
  }
  .brand-name {
    font-weight: 700;
    font-size: 68px;
    line-height: 1;
    letter-spacing: 6px;
    color: var(--teal);
  }
  .address {
    position: absolute;
    left: 418px;
    top: 134px;
    font-size: 26px;
    letter-spacing: 0.3px;
    white-space: nowrap;
  }
  .rule {
    position: absolute;
    left: 56px;
    top: 177px;
    width: 1085px;
    height: 8px;
    background: var(--teal);
  }
  .identity {
    position: absolute;
    left: 0;
    top: 318px;
    width: 1200px;
    text-align: center;
  }
  .person-name {
    margin: 0;
    font-size: 94px;
    font-weight: 700;
    line-height: 1;
    letter-spacing: 1px;
  }
  .person-title {
    margin: 18px 0 0;
    font-size: 43px;
    font-weight: 400;
    line-height: 1;
  }
  .swoosh {
    position: absolute;
    left: 0;
    top: 0;
  }
  .contact {
    position: absolute;
    right: 64px;
    top: 689px;
    text-align: right;
    color: var(--paper);
    font-weight: 700;
    font-size: 26px;
    line-height: 34px;
    letter-spacing: 0.3px;
  }
  .contact p { margin: 0; }
</style>
</head>
<body>
  <div class="card">
    <div class="brand">
      <div class="brand-square"></div>
      <div class="brand-name">QLT</div>
    </div>
    <div class="address">3-2-48 Kamiyoshi Nakarino 164-0392 Tokyo Japan</div>
    <div class="rule"></div>

    <div class="identity">
      <h1 class="person-name">Lukas Brenning</h1>
      <p class="person-title">Certified Meridian Guide</p>
    </div>

    <svg class="swoosh" width="1200" height="777" viewBox="0 0 1200 777" aria-hidden="true">
      <path d="M0,740 Q380,712 780,664 Q380,722 0,758 Z" fill="var(--teal-light)"/>
      <path d="M0,777 L0,765 Q420,742 740,668 Q990,612 1200,532 L1200,777 Z" fill="var(--teal)"/>
    </svg>

    <div class="contact">
      <p class="contact-phone">Phone: +81 70 4817 5062</p>
      <p class="contact-email">E-Mail: lukas.brenning@mailora.example</p>
    </div>
  </div>
</body>
</html>
```